KRW Flyer

Purpose: Will be an insert into Ironbrook Portals folder (picture of folder attached) given to clients who have purchased a residential or commercial access gate. Customers will be high end so the piece needs to speak to a high end customer (affluent). The goal is to give courtesy three month service call with the ultimate goal to secure a service contact. Pricing will vary by gate and gate traffic, so do not want to list pricing. Word Doc - V3 3 Month Courtesy Check Up has copy for flyer with suggestions for image placement.

```html
<!DOCTYPE html>
<html lang="en">
<head>
<meta charset="utf-8">
<title>KRW – 3 Month Courtesy Check-Up Insert</title>
<link rel="stylesheet" href="https://fonts.googleapis.com/css2?family=Quicksand:wght@400;500;700&display=swap">
<style>
  :root {
    --maroon: #7d1418;
    --ink: #3a3a3a;
    --paper-top: #f2f2f2;
    --paper-bottom: #e4e4e4;
    --band: #a9a9a9;
    --band-light: #d0d0d0;
    --stage: #5e5e5e;
    --frame: #8e8e8e;
  }
  * { box-sizing: border-box; margin: 0; padding: 0; }
  html, body { width: 946px; height: 1200px; overflow: hidden; }
  body {
    background: var(--stage);
    font-family: "Quicksand", sans-serif;
    color: var(--ink);
    position: relative;
  }
  .card {
    position: absolute;
    left: 122px;
    width: 708px;
    height: 502px;
    background: linear-gradient(180deg, var(--paper-top), var(--paper-bottom));
    overflow: hidden;
  }
  .card--front { top: 58px; }
  .card--back { top: 646px; }
  .abs { position: absolute; }

  .hero-photo {
    top: 0; left: 0; width: 708px; height: 166px;
    background: linear-gradient(180deg, #cfd3d6 0%, #e6e1d8 45%, #d9d3c7 75%, #c8cbc2 100%);
  }
  .band {
    left: 0; width: 708px; height: 14px;
    background: linear-gradient(180deg, var(--band-light), var(--band) 50%, var(--band-light));
  }
  .card--front .band { top: 166px; }

  .title-main {
    top: 190px; left: 0; width: 708px; text-align: center;
    font-weight: 700; font-size: 25px; color: var(--maroon); letter-spacing: 0.3px;
  }
  .section-title {
    left: 0; width: 708px; text-align: center;
    font-weight: 700; font-size: 15.5px; color: var(--maroon);
  }
  .sub-title { font-weight: 700; font-size: 13px; color: var(--maroon); }
  .intro {
    top: 231px; left: 13px; width: 690px;
    font-size: 9.6px; line-height: 12.2px;
  }
  .card--front .section-title { top: 280px; }
  .card--front .sub-title { top: 311px; left: 13px; }
  .reasons { top: 333px; left: 13px; width: 692px; list-style: none; font-size: 9.6px; line-height: 12.2px; }
  .reasons li { margin-bottom: 12px; padding-left: 9px; text-indent: -9px; }
  .reasons .sublist { list-style: none; margin: 0 0 0 22px; text-indent: 0; }
  .reasons .sublist li { margin: 0; padding: 0; text-indent: 0; }

  .card--back .section-title--plan { top: 10px; }
  .card--back .sub-title { top: 44px; left: 14px; font-size: 13.5px; }
  .dash-list { list-style: none; font-size: 9.6px; line-height: 12.2px; }
  .dash-list li { padding-left: 9px; text-indent: -9px; }
  .benefits { top: 63px; left: 14px; width: 420px; }
  .card--back .section-title--inspect { top: 181px; }
  .inspections { top: 205px; left: 14px; width: 600px; }
  .card--back .section-title--promise { top: 406px; }

  .photo-frame {
    left: 434px; width: 262px; height: 136px;
    border: 4px solid var(--frame);
  }
  .photo-frame--operator { top: 34px; background: linear-gradient(135deg, #6c8e4a 0%, #8a8f92 40%, #b7b9bb 70%, #9fa3a6 100%); }
  .photo-frame--entrance { top: 205px; background: linear-gradient(180deg, #4e8fd6 0%, #8fb2cf 35%, #d9dcd8 60%, #7ea55a 85%, #c6c6c4 100%); }

  .card--back .band { top: 430px; height: 5px; }
  .footer { top: 435px; left: 0; width: 708px; height: 67px; }
  .footer-brand {
    position: absolute; top: 22px; font-weight: 700; color: var(--maroon);
  }
  .footer-brand--portals { left: 16px; width: 90px; font-size: 10px; line-height: 12px; text-align: center; }
  .footer-brand--krw { right: 22px; font-size: 24px; }
  .footer-info {
    position: absolute; left: 180px; width: 350px; top: 6px;
    text-align: center; font-size: 6.2px; line-height: 8.2px;
  }
  .footer-info .strong { font-weight: 700; font-size: 6.6px; }
  .footer-info .split { display: flex; justify-content: space-between; padding: 0 6px; }
</style>
</head>
<body>

<section class="card card--front">
  <div class="abs hero-photo" role="img" aria-label="Photo of a white horizontal-slat aluminum sliding gate across a pale stone driveway"></div>
  <div class="abs band"></div>

  <h1 class="abs title-main">3 MONTH COURTESY CHECK-UP</h1>
  <p class="abs intro">Ironbrook Portals we will send out one of our skilled service technicians at three months after installation to make sure you are 100 percent satisfied, inspect your Custom Aluminum Gate / Access System and to answer any questions.</p>

  <h2 class="abs section-title">SERVICING YOUR AUTOMATED ELECTRIC GATE / ACCESS SYSTEM IS ESSENTIAL</h2>
  <h3 class="abs sub-title">Why Preventive Maintenance?</h3>
  <ul class="abs reasons">
    <li>- Automated gates are large, heavy and can be dangerous to work with. Like all mechanical systems they need regular maintenance to ensure proper operation and to prolong the life of your investment.</li>
    <li>- Regular inspections often catch problems while they are small. A major overhaul or having to replace major equipment can be very expensive.</li>
    <li>- A gate failure never comes at a good time, proper and regularly scheduled maintenance will help keep you from being caught stranded.</li>
    <li>- Business Owners:
      <ul class="sublist">
        <li>o Reduce costly downtime impact.</li>
        <li>o Capital repair / replacement planning.</li>
        <li>o Current and future facility usage.</li>
        <li>o Current and future business needs.</li>
      </ul>
    </li>
  </ul>
</section>

<section class="card card--back">
  <h2 class="abs section-title section-title--plan">ASK ABOUT A IRONBROOK PORTALS PLANNED MAINTENANCE PROGRAM</h2>
  <h3 class="abs sub-title">Program Benefits</h3>
  <ul class="abs dash-list benefits">
    <li>- Priority scheduling for service / repairs.</li>
    <li>- 10% discount on service calls and quoted repairs.</li>
    <li>- Decrease downtime.</li>
    <li>- Reduce probability of a gate or gate operator malfunction.</li>
    <li>- Extend the life of your gate / access system.</li>
    <li>- Ensure the safe operation of your equipment.</li>
    <li>- Decrease long term repair expense.</li>
    <li>- Each service call includes a written checklist of work performed, along with recommendations for any needed repairs or product replacement.</li>
  </ul>
  <div class="abs photo-frame photo-frame--operator" role="img" aria-label="Photo of a dark slatted sliding gate with its motor operator on a paver driveway"></div>

  <h2 class="abs section-title section-title--inspect">WHAT CAN YOU EXPECT OUR TECHNICIAN TO INSPECT?</h2>
  <ul class="abs dash-list inspections">
    <li>- Test for proper operation.</li>
    <li>- Visually inspect the rollers, fasteners, brackets, and other gate hardware<br>for proper alignment, proper tightness, and signs of damage, breakage,<br>looseness, rust or wear.</li>
    <li>- Check for secure mounting.</li>
    <li>- Check all sprockets and pulleys for alignment, tighten set screws as needed.</li>
    <li>- Oil or Grease bearings or chain.</li>
    <li>- Moving parts lubricated.</li>
    <li>- Check gear reducer oil level.</li>
    <li>- Check clutch and adjust as needed.</li>
    <li>- Tighten hinges or rollers as needed.</li>
    <li>- Check electrical connections.</li>
    <li>- Visually inspect wiring for fraying or exposure.</li>
    <li>- Test and inspect entrapment protection devices, edge sensors or photoelectric eyes.</li>
    <li>- Test manual release and manual release operation.</li>
    <li>- Provide detail quote for parts that require replacement.</li>
  </ul>
  <div class="abs photo-frame photo-frame--entrance" role="img" aria-label="Photo of a black slatted entrance gate between white pillars with palms and blue sky"></div>

  <h2 class="abs section-title section-title--promise">OUR REPUTATION IS YOUR PEACE OF MIND</h2>

  <div class="abs band"></div>
  <footer class="abs footer">
    <div class="footer-brand footer-brand--portals">Ironbrook Portals</div>
    <div class="footer-info">
      <div class="strong">RESIDENTIAL &nbsp;&nbsp; COMMERCIAL &nbsp;&nbsp; INDUSTRIAL</div>
      <div class="strong">CUSTOM ALUMINUM GATES / ACCESS SYSTEMS / AUTOMATIC OPENERS / SECURITY BARRIER ARMS</div>
      <div class="split"><span>Same Day and 24/7 Emergency Service Available</span><span>Visit our website: ironbrookportals.com</span></div>
      <div class="split"><span>555.014.2300</span><span>555.019.7699</span><span>555.014.7474</span></div>
      <div>Ironbrook Portals, a division of KRW, is a third generation family run business established in 1964.</div>
      <div>We thank all our customers for our growth and many years in business.</div>
    </div>
    <div class="footer-brand footer-brand--krw">KRW</div>
  </footer>
</section>

</body>
</html>
```